Stroomwacht Powerpoint - presentation slides for energy management tool

We need a Powerpoint presentation lay-out which matches our logo from Stroomwacht.nl. 10 slides variations minimum, enough for a full professional presentation to potential clients.
Stroomwacht is a Dutch energymanagement tool for corporate real estate and housing agency. Our clients are Social houseing organisation, real estate owers, property managers and property developers.
Target Market(s)
real estate owners
Property manage
Font styles to use
Sans Serif
Colors
f78f20
0255a3
Requirements
Must have
- Stroomwacht logo colors and style
#F37122 orange
#00345D darkblue
Nice to have
- Professional look, background not white in every slide
Should not have
- wrong color orange and blue.

```html
<!DOCTYPE html>
<html lang="nl">
<head>
<meta charset="utf-8">
<title>Stroomwacht presentatie – slide-overzicht</title>
<link href="https://fonts.googleapis.com/css2?family=Open+Sans:wght@300;400;600;700&display=swap" rel="stylesheet">
<style>
:root{
  --orange:#F37122;
  --navy:#00345D;
  --navy-deep:#0b2a4a;
  --stage:#a7a7a7;
  --ink:#4a4f57;
  --white:#ffffff;
  --ph-city:linear-gradient(165deg,#4a6d94 0%,#1e3a5e 55%,#0e223b 100%);
  --ph-office:linear-gradient(135deg,#d3d6da 0%,#9aa1aa 100%);
  --ph-people:linear-gradient(135deg,#ddd3c8 0%,#9a8a7c 100%);
  --ph-building:linear-gradient(180deg,#a9c1d7 0%,#7493ad 55%,#557f44 100%);
  --ph-orange:linear-gradient(135deg,#f5894a 0%,#e0651d 100%);
}
*{box-sizing:border-box;margin:0;padding:0}
html,body{width:1200px;height:1083px;overflow:hidden;background:var(--stage)}
body{font-family:"Open Sans",Arial,sans-serif;color:var(--ink)}
.deck{position:absolute;left:77px;top:59px;display:grid;grid-template-columns:repeat(4,238px);grid-auto-rows:134px;column-gap:33px;row-gap:31px}
.slide{position:relative;width:238px;height:134px;overflow:hidden;background:var(--white)}
.abs{position:absolute}
.photo{position:absolute}
.ph-city{background:var(--ph-city)}
.ph-office{background:var(--ph-office)}
.ph-people{background:var(--ph-people)}
.ph-building{background:var(--ph-building)}
.ph-orange{background:var(--ph-orange)}
.bg-navy{background:var(--navy)}
.bg-orange{background:var(--orange)}
.body-text{font-size:3.1px;line-height:1.4;color:var(--ink)}
.body-text.light{color:#dfe7f0}
.slide-title{font-size:6.5px;font-weight:700;color:var(--navy);letter-spacing:.1px}
.item-title{font-size:3.9px;font-weight:700;color:var(--navy);margin-bottom:1px}
.item-title.orange{color:var(--orange)}
.item-title.white{color:var(--white)}
.tag{display:inline-block;background:var(--orange);color:var(--white);font-size:3.2px;font-weight:700;padding:1px 3px;margin-bottom:2px}
.quote{font-weight:700;text-align:center;line-height:1.3}
.icon{width:14px;height:14px;color:var(--orange)}
.icon.white{color:var(--white)}
.logo{display:flex;align-items:center;gap:2px;font-size:4px;font-weight:700;color:var(--orange)}
.logo .dot{width:5px;height:5px;border-radius:50%;background:var(--orange)}
.item{position:absolute;display:flex;gap:4px}
.avatar{position:absolute;border-radius:50%;background:var(--ph-people)}
.footer-line{position:absolute;left:14px;right:8px;bottom:5px;height:.5px;background:#d5d8dc}
</style>
</head>
<body>
<svg width="0" height="0" style="position:absolute">
  <defs>
    <symbol id="i-chart" viewBox="0 0 24 24"><rect x="3" y="3" width="18" height="14" fill="none" stroke="currentColor" stroke-width="1.5"/><rect x="6" y="11" width="2.5" height="4" fill="currentColor"/><rect x="10.5" y="8" width="2.5" height="7" fill="currentColor"/><rect x="15" y="6" width="2.5" height="9" fill="currentColor"/><path d="M9 21h6M12 17v4" stroke="currentColor" stroke-width="1.5"/></symbol>
    <symbol id="i-doc" viewBox="0 0 24 24"><rect x="5" y="3" width="14" height="18" fill="none" stroke="currentColor" stroke-width="1.5"/><path d="M8 8h8M8 12h8M8 16h5" stroke="currentColor" stroke-width="1.5"/></symbol>
    <symbol id="i-people" viewBox="0 0 24 24"><circle cx="7" cy="8" r="2.5" fill="currentColor"/><circle cx="17" cy="8" r="2.5" fill="currentColor"/><circle cx="12" cy="11" r="3" fill="currentColor"/><path d="M2 18c0-3 2-5 5-5s5 2 5 5zM12 18c0-3 2-5 5-5s5 2 5 5zM6 21c0-3 3-6 6-6s6 3 6 6z" fill="currentColor"/></symbol>
    <symbol id="i-lock" viewBox="0 0 24 24"><rect x="5" y="10" width="14" height="11" rx="1" fill="currentColor"/><path d="M8 10V7a4 4 0 0 1 8 0v3" fill="none" stroke="currentColor" stroke-width="2"/></symbol>
    <symbol id="i-play" viewBox="0 0 24 24"><rect x="3" y="5" width="18" height="13" fill="none" stroke="currentColor" stroke-width="1.5"/><path d="M10 8.5v6l5-3z" fill="currentColor"/><path d="M8 21h8" stroke="currentColor" stroke-width="1.5"/></symbol>
    <symbol id="i-building" viewBox="0 0 24 24"><rect x="4" y="6" width="16" height="15" fill="currentColor"/><path d="M7 9h2M11 9h2M15 9h2M7 13h2M11 13h2M15 13h2M7 17h2M15 17h2" stroke="#fff" stroke-width="1.5"/><path d="M2 6l10-4 10 4z" fill="currentColor"/></symbol>
    <symbol id="i-cap" viewBox="0 0 24 24"><path d="M1 9l11-5 11 5-11 5z" fill="currentColor"/><path d="M6 12v4c2 2 10 2 12 0v-4l-6 3z" fill="currentColor"/></symbol>
    <symbol id="i-calendar" viewBox="0 0 24 24"><rect x="3" y="5" width="18" height="16" rx="2" fill="currentColor"/><path d="M7 3v4M17 3v4" stroke="currentColor" stroke-width="2"/><rect x="5" y="10" width="14" height="9" fill="#fff" opacity=".25"/></symbol>
    <symbol id="i-download" viewBox="0 0 24 24"><path d="M12 2l9 5v10l-9 5-9-5V7z" fill="currentColor"/><path d="M12 7v7M9 11l3 3 3-3" fill="none" stroke="#0b2a4a" stroke-width="1.8"/></symbol>
  </defs>
</svg>

<main class="deck">

  <!-- 1 cover -->
  <section class="slide">
    <div class="photo ph-city" style="inset:0" role="img" aria-label="Skyline van een stad bij schemering"></div>
    <div class="abs" style="left:95px;top:0;width:48px;height:21px;background:#fff;border-radius:0 0 4px 4px;display:flex;align-items:center;justify-content:center">
      <div class="logo"><span class="dot"></span>Stroomwacht</div>
    </div>
    <h1 class="abs" style="left:18px;right:18px;top:62px;font-size:8.4px;font-weight:600;color:#fff;text-align:center;line-height:1.4">Beste platform voor het beheren van meters binnen uw gebouwenportfolio</h1>
  </section>

  <!-- 2 introduction -->
  <section class="slide bg-navy">
    <div class="photo ph-people" style="left:0;top:0;width:119px;height:134px" role="img" aria-label="Twee collega's overleggen aan een bureau"></div>
    <h2 class="abs" style="left:140px;top:33px;font-size:7px;font-weight:600;color:#fff">Introduction</h2>
    <p class="abs body-text light" style="left:140px;top:47px;width:88px">Lorem ipsum dolor sit amet, consectetur adipiscing elit, sed do eiusmod tempor incididunt ut labore et dolore magna aliqua. Ut enim ad minim veniam, quis nostrud exercitation ullamco laboris nisi ut aliquip ex ea commodo consequat. Lorem ipsum dolor sit amet, consectetur adipiscing elit, sed do eiusmod tempor incididunt ut labore et dolore magna aliqua. Ut enim ad minim veniam, quis nostrud exercitation ullamco laboris nisi ut aliquip ex ea commodo consequat.</p>
  </section>

  <!-- 3 about us -->
  <section class="slide">
    <div class="photo ph-building" style="inset:0" role="img" aria-label="Glazen kantoorgebouw met bomen"></div>
    <div class="abs" style="left:22px;top:0;width:94px;height:112px;background:#fff;padding:20px 10px 0">
      <h2 style="font-size:7.5px;font-weight:600;color:var(--navy);margin-bottom:4px">About Us</h2>
      <p class="body-text">Lorem ipsum dolor sit amet, consectetur adipiscing elit, sed do eiusmod tempor incididunt ut labore et dolore magna aliqua. Ut enim ad minim veniam, quis nostrud exercitation ullamco laboris nisi ut aliquip ex ea commodo consequat. Lorem ipsum dolor sit amet, consectetur adipiscing elit, sed do eiusmod.</p>
    </div>
  </section>

  <!-- 4 portfolio -->
  <section class="slide">
    <div class="photo ph-office" style="left:0;top:0;width:108px;height:134px" role="img" aria-label="Medewerkers achter beeldschermen in een kantoor"></div>
    <h2 class="abs slide-title" style="left:150px;top:12px">OUR PORTFOLIO</h2>
    <div class="item" style="left:124px;top:32px;width:104px"><svg class="icon"><use href="#i-chart"/></svg><div><div class="item-title orange">Lorem Ipsum</div><p class="body-text">Lorem ipsum dolor sit amet, consectetur adipiscing elit, sed do eiusmod tempor incididunt ut labore et dolore magna aliqua.</p></div></div>
    <div class="item" style="left:124px;top:65px;width:104px"><svg class="icon"><use href="#i-calendar"/></svg><div><div class="item-title orange">Lorem Ipsum</div><p class="body-text">Lorem ipsum dolor sit amet, consectetur adipiscing elit, sed do eiusmod tempor incididunt ut labore et dolore magna aliqua.</p></div></div>
    <div class="item" style="left:124px;top:98px;width:104px"><svg class="icon"><use href="#i-doc"/></svg><div><div class="item-title orange">Lorem Ipsum</div><p class="body-text">Lorem ipsum dolor sit amet, consectetur adipiscing elit, sed do eiusmod tempor incididunt ut labore et dolore magna aliqua.</p></div></div>
  </section>

  <!-- 5 navy panel with features -->
  <section class="slide">
    <div class="photo ph-city" style="inset:0" role="img" aria-label="Stadsgezicht met beursgrafieken in blauw"></div>
    <div class="abs bg-navy" style="left:0;top:0;width:70px;height:134px;padding:29px 9px 0 17px">
      <h2 style="font-size:5.5px;font-weight:600;color:#fff;margin-bottom:3px">Lorem Ipsum</h2>
      <p class="body-text light">Lorem ipsum dolor sit amet, consectetur adipiscing elit, sed do eiusmod tempor incididunt ut labore et dolore magna aliqua. Ut enim ad minim veniam, quis nostrud exercitation ullamco laboris nisi ut aliquip ex ea commodo consequat. Lorem ipsum dolor sit amet, consectetur adipiscing elit, sed do eiusmod tempor incididunt ut labore et dolore magna aliqua. Ut enim ad minim veniam, quis nostrud exercitation ullamco laboris nisi ut aliquip ex ea commodo consequat.</p>
    </div>
    <div class="abs" style="left:70px;top:22px;width:149px;height:94px;background:#fff"></div>
    <div class="abs" style="left:88px;top:32px;width:56px"><svg class="icon" style="width:9px;height:9px"><use href="#i-play"/></svg><div class="item-title">Lorem Ipsum</div><p class="body-text">Lorem ipsum dolor sit amet, consectetur adipiscing elit, sed do eiusmod.</p></div>
    <div class="abs" style="left:155px;top:32px;width:56px"><svg class="icon" style="width:9px;height:9px"><use href="#i-chart"/></svg><div class="item-title">Lorem Ipsum</div><p class="body-text">Lorem ipsum dolor sit amet, consectetur adipiscing elit, sed do eiusmod.</p></div>
    <div class="abs" style="left:88px;top:74px;width:56px"><svg class="icon" style="width:9px;height:9px"><use href="#i-cap"/></svg><div class="item-title">Lorem Ipsum</div><p class="body-text">Lorem ipsum dolor sit amet, consectetur adipiscing elit, sed do eiusmod.</p></div>
    <div class="abs" style="left:155px;top:74px;width:56px"><svg class="icon" style="width:9px;height:9px"><use href="#i-lock"/></svg><div class="item-title">Lorem Ipsum</div><p class="body-text">Lorem ipsum dolor sit amet, consectetur adipiscing elit, sed do eiusmod.</p></div>
  </section>

  <!-- 6 meet our team -->
  <section class="slide">
    <h2 class="abs slide-title" style="left:14px;top:13px">MEET OUR TEAM</h2>
    <div class="abs" style="left:14px;top:27px;width:212px;display:grid;grid-template-columns:repeat(6,1fr);gap:2px">
      <div><div class="ph-people" style="height:72px" role="img" aria-label="Portret teamlid"></div><div class="bg-orange" style="height:16px;color:#fff;text-align:center;padding-top:3px;font-size:3.2px;font-weight:700">Ruben Kok<div style="font-weight:400;font-size:2.6px">CEO/President</div></div></div>
      <div><div class="ph-people" style="height:72px" role="img" aria-label="Portret teamlid"></div><div class="bg-orange" style="height:16px;color:#fff;text-align:center;padding-top:3px;font-size:3.2px;font-weight:700">Eva Bos<div style="font-weight:400;font-size:2.6px">VP-Finance</div></div></div>
      <div><div class="ph-people" style="height:72px" role="img" aria-label="Portret teamlid"></div><div class="bg-orange" style="height:16px;color:#fff;text-align:center;padding-top:3px;font-size:3.2px;font-weight:700">Sara Dijk<div style="font-weight:400;font-size:2.6px">Human Resource</div></div></div>
      <div><div class="ph-people" style="height:72px" role="img" aria-label="Portret teamlid"></div><div class="bg-orange" style="height:16px;color:#fff;text-align:center;padding-top:3px;font-size:3.2px;font-weight:700">Noor Vos<div style="font-weight:400;font-size:2.6px">Managing Director</div></div></div>
      <div><div class="ph-people" style="height:72px" role="img" aria-label="Portret teamlid"></div><div class="bg-orange" style="height:16px;color:#fff;text-align:center;padding-top:3px;font-size:3.2px;font-weight:700">Daan Smit<div style="font-weight:400;font-size:2.6px">Manager-Delivery</div></div></div>
      <div><div class="ph-people" style="height:72px" role="img" aria-label="Portret teamlid"></div><div class="bg-orange" style="height:16px;color:#fff;text-align:center;padding-top:3px;font-size:3.2px;font-weight:700">Lars Mol<div style="font-weight:400;font-size:2.6px">Manager-Accounts</div></div></div>
    </div>
    <div class="footer-line"></div>
  </section>

  <!-- 7 our services -->
  <section class="slide">
    <h2 class="abs slide-title" style="left:14px;top:13px">OUR SERVICES</h2>
    <div class="item" style="left:14px;top:32px;width:70px"><svg class="icon"><use href="#i-chart"/></svg><div><div class="item-title">Lorem ipsum dolor</div><p class="body-text">Lorem ipsum dolor sit amet, consectetur adipiscing elit, sed do eiusmod.</p></div></div>
    <div class="item" style="left:86px;top:32px;width:70px"><svg class="icon"><use href="#i-doc"/></svg><div><div class="item-title">Lorem ipsum dolor</div><p class="body-text">Lorem ipsum dolor sit amet, consectetur adipiscing elit, sed do eiusmod.</p></div></div>
    <div class="item" style="left:14px;top:64px;width:70px"><svg class="icon"><use href="#i-people"/></svg><div><div class="item-title">Lorem ipsum dolor</div><p class="body-text">Lorem ipsum dolor sit amet, consectetur adipiscing elit, sed do eiusmod.</p></div></div>
    <div class="item" style="left:86px;top:64px;width:70px"><svg class="icon"><use href="#i-calendar"/></svg><div><div class="item-title">Lorem ipsum dolor</div><p class="body-text">Lorem ipsum dolor sit amet, consectetur adipiscing elit, sed do eiusmod.</p></div></div>
    <div class="item" style="left:14px;top:96px;width:70px"><svg class="icon"><use href="#i-doc"/></svg><div><div class="item-title">Lorem ipsum dolor</div><p class="body-text">Lorem ipsum dolor sit amet, consectetur adipiscing elit, sed do eiusmod.</p></div></div>
    <div class="item" style="left:86px;top:96px;width:70px"><svg class="icon"><use href="#i-people"/></svg><div><div class="item-title">Lorem ipsum dolor</div><p class="body-text">Lorem ipsum dolor sit amet, consectetur adipiscing elit, sed do eiusmod.</p></div></div>
    <div class="photo ph-people" style="left:159px;top:12px;width:71px;height:112px" role="img" aria-label="Vrouw met laptop"></div>
    <div class="footer-line"></div>
  </section>

  <!-- 8 testimonials -->
  <section class="slide">
    <div class="abs bg-orange" style="left:0;top:0;width:99px;height:134px;padding:22px 12px 0;color:#fff">
      <div style="font-size:22px;font-weight:700;text-align:center;line-height:.8">“</div>
      <p class="quote" style="font-size:4.6px;margin-top:4px">“Lorem ipsum dolor sit amet, consectetur adipiscing elit. Phasellus sodales, ligula ultrices tempus ristique, tellus justo aliquam dui, nec Lorem ipsum dolor sit amet, consectetur</p>
    </div>
    <h2 class="abs slide-title" style="left:111px;top:12px">TESTIMONIALS</h2>
    <div class="avatar" style="left:112px;top:32px;width:20px;height:20px" role="img" aria-label="Portret klant"></div>
    <div class="abs" style="left:141px;top:33px;width:88px"><div class="item-title">Lorem Ipsum</div><p class="body-text">Lorem ipsum dolor sit amet, consectetur adipiscing elit, sed do eiusmod tempor incididunt ut labore et dolore magna aliqua.</p></div>
    <div class="avatar" style="left:112px;top:65px;width:20px;height:20px" role="img" aria-label="Portret klant"></div>
    <div class="abs" style="left:141px;top:66px;width:88px"><div class="item-title">Lorem Ipsum</div><p class="body-text">Lorem ipsum dolor sit amet, consectetur adipiscing elit, sed do eiusmod tempor incididunt ut labore et dolore magna aliqua.</p></div>
    <div class="avatar" style="left:112px;top:98px;width:20px;height:20px" role="img" aria-label="Portret klant"></div>
    <div class="abs" style="left:141px;top:99px;width:88px"><div class="item-title">Lorem Ipsum</div><p class="body-text">Lorem ipsum dolor sit amet, consectetur adipiscing elit, sed do eiusmod tempor incididunt ut labore et dolore magna aliqua.</p></div>
  </section>

  <!-- 9 quote column -->
  <section class="slide">
    <div class="photo ph-orange" style="left:83px;top:0;width:74px;height:134px" role="img" aria-label="Stadsgezicht in oranje tint"></div>
    <p class="abs quote" style="left:88px;top:28px;width:64px;font-size:5.2px;color:#fff">“Lorem ipsum dolor sit amet, consectetur adipiscing elit. Phasellus sodales, ligula ultrices tempus ristique, tellus justo aliquam dui,</p>
    <div class="abs" style="left:22px;top:26px;width:56px;text-align:right"><span class="tag">Lorem Ipsum</span><p class="body-text">Lorem ipsum dolor sit amet, consectetur adipiscing elit, sed do eiusmod tempor incididunt ut labore et dolore magna aliqua.</p></div>
    <div class="abs" style="left:22px;top:80px;width:56px;text-align:right"><span class="tag">Lorem Ipsum</span><p class="body-text">Lorem ipsum dolor sit amet, consectetur adipiscing elit, sed do eiusmod tempor incididunt ut labore et dolore magna aliqua.</p></div>
    <div class="abs" style="left:172px;top:26px;width:56px"><span class="tag">Lorem Ipsum</span><p class="body-text">Lorem ipsum dolor sit amet, consectetur adipiscing elit, sed do eiusmod tempor incididunt ut labore et dolore magna aliqua.</p></div>
    <div class="abs" style="left:172px;top:80px;width:56px"><span class="tag">Lorem Ipsum</span><p class="body-text">Lorem ipsum dolor sit amet, consectetur adipiscing elit, sed do eiusmod tempor incididunt ut labore et dolore magna aliqua.</p></div>
  </section>

  <!-- 10 our team cards -->
  <section class="slide">
    <h2 class="abs slide-title" style="left:0;right:0;top:12px;text-align:center">OUR TEAM</h2>
    <div class="photo ph-office" style="left:0;top:28px;width:238px;height:56px" role="img" aria-label="Werkplek van bovenaf met laptops"></div>
    <div class="abs" style="left:0;top:56px;width:238px;height:28px;background:rgba(0,52,93,.75)"></div>
    <div class="abs bg-orange" style="left:21px;top:56px;width:57px;height:34px;text-align:center;padding-top:6px;color:#fff"><svg class="icon white" style="width:13px;height:13px"><use href="#i-chart"/></svg><div style="font-size:3.6px;font-weight:600;margin-top:2px">Lorem Ipsum Dolor</div></div>
    <div class="abs bg-orange" style="left:90px;top:56px;width:57px;height:34px;text-align:center;padding-top:6px;color:#fff"><svg class="icon white" style="width:13px;height:13px"><use href="#i-building"/></svg><div style="font-size:3.6px;font-weight:600;margin-top:2px">Lorem Ipsum Dolor</div></div>
    <div class="abs bg-orange" style="left:159px;top:56px;width:57px;height:34px;text-align:center;padding-top:6px;color:#fff"><svg class="icon white" style="width:13px;height:13px"><use href="#i-people"/></svg><div style="font-size:3.6px;font-weight:600;margin-top:2px">Lorem Ipsum Dolor</div></div>
    <p class="abs body-text" style="left:21px;top:94px;width:57px;text-align:center;color:#222">Lorem ipsum dolor sit amet, consectetur adipiscing elit, sed do eiusmod.</p>
    <p class="abs body-text" style="left:90px;top:94px;width:57px;text-align:center;color:#222">Lorem ipsum dolor sit amet, consectetur adipiscing elit, sed do eiusmod.</p>
    <p class="abs body-text" style="left:159px;top:94px;width:57px;text-align:center;color:#222">Lorem ipsum dolor sit amet, consectetur adipiscing elit, sed do eiusmod.</p>
  </section>

  <!-- 11 quote, photo, features -->
  <section class="slide">
    <p class="abs quote" style="left:6px;top:38px;width:50px;font-size:5.6px;color:var(--navy)">“Lorem ipsum dolor sit amet, consectetur adipiscing elit.</p>
    <div class="photo ph-people" style="left:60px;top:0;width:90px;height:134px" role="img" aria-label="Vrouw met laptop"></div>
    <div class="item" style="left:162px;top:18px;width:70px"><svg class="icon" style="width:9px;height:9px;flex:none"><use href="#i-lock"/></svg><div><div class="item-title">Lorem Ipsum Dolor</div><p class="body-text">Lorem ipsum dolor sit amet, consectetur adipiscing elit, sed do eiusmod tempor incididunt ut labore et dolore magna aliqua.</p></div></div>
    <div class="item" style="left:162px;top:57px;width:70px"><svg class="icon" style="width:9px;height:9px;flex:none"><use href="#i-people"/></svg><div><div class="item-title">Lorem Ipsum Dolor</div><p class="body-text">Lorem ipsum dolor sit amet, consectetur adipiscing elit, sed do eiusmod tempor incididunt ut labore et dolore magna aliqua.</p></div></div>
    <div class="item" style="left:162px;top:96px;width:70px"><svg class="icon" style="width:9px;height:9px;flex:none"><use href="#i-cap"/></svg><div><div class="item-title">Lorem Ipsum Dolor</div><p class="body-text">Lorem ipsum dolor sit amet, consectetur adipiscing elit, sed do eiusmod tempor incididunt ut labore et dolore magna aliqua.</p></div></div>
  </section>

  <!-- 12 orange band with three icons -->
  <section class="slide">
    <div class="photo ph-orange" style="left:0;top:0;width:238px;height:62px" role="img" aria-label="Vergaderzaal in oranje tint"></div>
    <p class="abs quote" style="left:20px;right:20px;top:24px;font-size:4.8px;color:#fff;font-weight:600">“Lorem ipsum dolor sit amet, consectetur adipiscing elit. Phasellus sodales, ligula ultrices tempus ristique, tellus justo aliquam dui,</p>
    <div class="abs" style="left:20px;top:73px;width:62px;text-align:center"><svg class="icon" style="color:var(--navy);width:18px;height:18px"><use href="#i-chart"/></svg><div class="item-title">Lorem Ipsum</div><p class="body-text">Lorem ipsum dolor sit amet, consectetur adipiscing elit, sed do eiusmod.</p></div>
    <div class="abs" style="left:88px;top:73px;width:62px;text-align:center"><svg class="icon" style="color:var(--navy);width:18px;height:18px"><use href="#i-doc"/></svg><div class="item-title">Lorem Ipsum</div><p class="body-text">Lorem ipsum dolor sit amet, consectetur adipiscing elit, sed do eiusmod.</p></div>
    <div class="abs" style="left:156px;top:73px;width:62px;text-align:center"><svg class="icon" style="color:var(--navy);width:18px;height:18px"><use href="#i-calendar"/></svg><div class="item-title">Lorem Ipsum</div><p class="body-text">Lorem ipsum dolor sit amet, consectetur adipiscing elit, sed do eiusmod.</p></div>
    <div class="abs logo" style="left:7px;bottom:5px;font-size:3px"><span class="dot" style="width:4px;height:4px"></span>Stroomwacht</div>
  </section>

  <!-- 13 collage with text -->
  <section class="slide">
    <div class="abs" style="left:0;top:0;width:139px;height:134px;display:grid;grid-template-columns:repeat(3,1fr);grid-template-rows:repeat(3,1fr);gap:1.5px">
      <div class="ph-office" role="img" aria-label="Vergaderruimte"></div>
      <div class="ph-people" role="img" aria-label="Overleg aan tafel"></div>
      <div class="ph-office" role="img" aria-label="Laptops op tafel"></div>
      <div class="ph-people" role="img" aria-label="Handen op bureau"></div>
      <div class="ph-office" role="img" aria-label="Team aan het werk"></div>
      <div class="ph-people" role="img" aria-label="Juichende medewerker"></div>
      <div class="ph-people" role="img" aria-label="Collega in gesprek"></div>
      <div class="ph-office" role="img" aria-label="Medewerker achter laptop"></div>
      <div class="ph-people" role="img" aria-label="Overleg in kantoor"></div>
    </div>
    <h2 class="abs" style="left:164px;top:21px;font-size:6.8px;font-weight:600;color:var(--navy)">Lorem Ipsum</h2>
    <p class="abs body-text" style="left:155px;top:33px;width:72px;text-align:center;color:#222">Lorem ipsum dolor sit amet, consectetur adipiscing elit, sed do eiusmod tempor incididunt ut labore et dolore magna aliqua. Ut enim ad minim veniam, quis nostrud exercitation ullamco laboris nisi ut aliquip ex ea commodo consequat. Lorem ipsum dolor sit amet, consectetur adipiscing elit, sed do eiusmod tempor incididunt ut labore et dolore magna aliqua. Ut enim ad minim veniam, quis nostrud exercitation ullamco laboris nisi ut aliquip ex ea commodo consequat.</p>
  </section>

  <!-- 14 executive leadership -->
  <section class="slide">
    <h2 class="abs slide-title" style="left:0;right:0;top:12px;text-align:center">EXECUTIVE LEADERSHIP</h2>
    <div class="avatar" style="left:21px;top:34px;width:36px;height:36px" role="img" aria-label="Portret bestuurder"></div>
    <div class="abs" style="left:61px;top:37px;width:50px"><span class="tag">Lorem Ipsum</span><p class="body-text">Lorem ipsum dolor sit amet, consectetur adipiscing elit, sed do eiusmod.</p></div>
    <div class="avatar" style="left:131px;top:34px;width:36px;height:36px" role="img" aria-label="Portret bestuurder"></div>
    <div class="abs" style="left:171px;top:37px;width:50px"><span class="tag">Lorem Ipsum</span><p class="body-text">Lorem ipsum dolor sit amet, consectetur adipiscing elit, sed do eiusmod.</p></div>
    <div class="avatar" style="left:21px;top:79px;width:36px;height:36px" role="img" aria-label="Portret bestuurder"></div>
    <div class="abs" style="left:61px;top:82px;width:50px"><span class="tag">Lorem Ipsum</span><p class="body-text">Lorem ipsum dolor sit amet, consectetur adipiscing elit, sed do eiusmod.</p></div>
    <div class="avatar" style="left:131px;top:79px;width:36px;height:36px" role="img" aria-label="Portret bestuurder"></div>
    <div class="abs" style="left:171px;top:82px;width:50px"><span class="tag">Lorem Ipsum</span><p class="body-text">Lorem ipsum dolor sit amet, consectetur adipiscing elit, sed do eiusmod.</p></div>
  </section>

  <!-- 15 photo band with statement -->
  <section class="slide">
    <div class="photo" style="left:16px;top:0;width:210px;height:62px;background:linear-gradient(135deg,#5d7796,#2d4a6e)" role="img" aria-label="Team in overleg rond een tafel"></div>
    <div class="abs" style="left:16px;top:81px;width:58px;height:.6px;background:var(--navy)"></div>
    <p class="abs quote" style="left:16px;top:86px;width:60px;font-size:4.8px;font-weight:600;color:var(--navy)">“Lorem ipsum dolor sit amet, consectetur</p>
    <div class="abs" style="left:16px;top:100px;width:58px;height:.6px;background:var(--navy)"></div>
    <p class="abs body-text" style="left:86px;top:71px;width:140px;color:#222">Lorem ipsum dolor sit amet, consectetur adipiscing elit, sed do eiusmod tempor incididunt ut labore et dolore magna aliqua. Ut enim ad minim veniam, quis nostrud exercitation ullamco laboris nisi ut aliquip ex ea commodo consequat. Lorem ipsum dolor sit amet, consectetur adipiscing elit, sed do eiusmod tempor incididunt ut labore et dolore magna aliqua. Ut enim ad minim veniam, quis nostrud exercitation ullamco laboris nisi ut aliquip ex ea commodo consequat.</p>
    <div class="footer-line"></div>
  </section>

  <!-- 16 section title -->
  <section class="slide">
    <div class="photo" style="inset:0;background:linear-gradient(160deg,#2b4d75 0%,#123358 55%,#0b2643 100%)" role="img" aria-label="Kantoor in donkerblauwe tint"></div>
    <h2 class="abs" style="left:0;right:0;top:58px;text-align:center;font-size:12px;font-weight:700;color:#fff">SECTION TITLE HERE</h2>
  </section>

  <!-- 17 edit title with skyline -->
  <section class="slide">
    <div class="abs bg-orange" style="left:0;top:0;width:238px;height:52px;padding:12px 14px 0;color:#fff">
      <h2 style="font-size:6.4px;font-weight:700;margin-bottom:2px">EDIT TITLE HERE</h2>
      <p class="body-text" style="color:#fff;width:118px;font-weight:600">Lorem ipsum dolor sit amet, consectetur adipiscing elit, sed do eiusmod tempor incididunt ut labore et dolore magna aliqua.</p>
    </div>
    <div class="photo ph-building" style="left:142px;top:20px;width:86px;height:103px" role="img" aria-label="Skyline aan het water"></div>
    <h3 class="abs" style="left:13px;top:60px;font-size:4.6px;font-weight:600;color:var(--navy)">Lorem ipsum dolor sit amet</h3>
    <p class="abs body-text" style="left:13px;top:68px;width:122px;color:#222">Lorem ipsum dolor sit amet, consectetur adipiscing elit, sed do eiusmod tempor incididunt ut labore et dolore magna aliqua. Ut enim ad minim veniam, quis nostrud exercitation ullamco laboris nisi ut aliquip ex ea commodo consequat. Lorem ipsum dolor sit amet, consectetur adipiscing elit, sed do eiusmod tempor incididunt ut labore et dolore magna aliqua. Ut enim ad minim veniam, quis nostrud exercitation ullamco laboris nisi ut aliquip ex ea commodo consequat.</p>
    <div class="abs logo" style="left:7px;bottom:5px;font-size:3px"><span class="dot" style="width:4px;height:4px"></span>Stroomwacht</div>
  </section>

  <!-- 18 navy text with desk photo -->
  <section class="slide bg-navy">
    <h2 class="abs" style="left:15px;top:30px;font-size:6.8px;font-weight:600;color:#fff">Lorem ipsum dolor sit</h2>
    <p class="abs body-text light" style="left:15px;top:43px;width:100px">Lorem ipsum dolor sit amet, consectetur adipiscing elit, sed do eiusmod tempor incididunt ut labore et dolore magna aliqua. Ut enim ad minim veniam, quis nostrud exercitation ullamco laboris nisi ut aliquip ex ea commodo consequat. Lorem ipsum dolor sit amet, consectetur adipiscing elit, sed do eiusmod tempor incididunt ut labore et dolore magna aliqua. Ut enim ad minim veniam, quis nostrud exercitation ullamco laboris nisi ut aliquip ex ea commodo consequat.</p>
    <div class="photo ph-office" style="left:126px;top:0;width:112px;height:134px" role="img" aria-label="Handen aan een bureau met laptops van bovenaf"></div>
  </section>

  <!-- 19 edit title with night city -->
  <section class="slide">
    <h2 class="abs slide-title" style="left:14px;top:12px">EDIT TITLE HERE</h2>
    <div class="photo" style="left:14px;top:28px;width:211px;height:62px;background:linear-gradient(180deg,#6f8fb3 0%,#3a4f6e 60%,#c98a4a 100%)" role="img" aria-label="Stad bij avond met verkeer"></div>
    <div class="item" style="left:18px;top:98px;width:100px"><svg class="icon" style="flex:none"><use href="#i-people"/></svg><div><div class="item-title">Lorem Ipsum</div><p class="body-text">Lorem ipsum dolor sit amet, consectetur adipiscing elit, sed do eiusmod tempor incididunt ut labore et dolore magna aliqua.</p></div></div>
    <div class="item" style="left:124px;top:98px;width:100px"><svg class="icon" style="flex:none"><use href="#i-play"/></svg><div><div class="item-title">Lorem Ipsum</div><p class="body-text">Lorem ipsum dolor sit amet, consectetur adipiscing elit, sed do eiusmod tempor incididunt ut labore et dolore magna aliqua.</p></div></div>
    <div class="footer-line"></div>
  </section>

  <!-- 20 quote, navy list, tablet photo -->
  <section class="slide">
    <p class="abs quote" style="left:4px;top:38px;width:48px;font-size:5.4px;font-weight:600;color:var(--navy)">“Lorem ipsum dolor sit amet, consectetur adipiscing</p>
    <div class="photo" style="left:120px;top:0;width:118px;height:134px;background:linear-gradient(135deg,#8fa4ba,#3f5670)" role="img" aria-label="Handen met een tablet"></div>
    <div class="abs bg-navy" style="left:55px;top:0;width:88px;height:134px;padding:13px 8px 0 12px">
      <div style="margin-bottom:8px"><div class="item-title white">Lorem Ipsum Dolor</div><p class="body-text light">Lorem ipsum dolor sit amet, consectetur adipiscing elit, sed do eiusmod tempor incididunt ut labore et dolore magna aliqua.</p></div>
      <div style="margin-bottom:8px"><div class="item-title white">Lorem Ipsum Dolor</div><p class="body-text light">Lorem ipsum dolor sit amet, consectetur adipiscing elit, sed do eiusmod tempor incididunt ut labore et dolore magna aliqua.</p></div>
      <div><div class="item-title white">Lorem Ipsum Dolor</div><p class="body-text light">Lorem ipsum dolor sit amet, consectetur adipiscing elit, sed do eiusmod tempor incididunt ut labore et dolore magna aliqua.</p></div>
    </div>
  </section>

  <!-- 21 navy text with features -->
  <section class="slide">
    <div class="abs bg-navy" style="left:0;top:0;width:124px;height:134px;padding:22px 14px 0 16px">
      <h2 style="font-size:6.8px;font-weight:600;color:#fff;line-height:1.3;margin-bottom:4px">Lorem ipsum dolor<br>sit amet, consectetur</h2>
      <p class="body-text light">Lorem ipsum dolor sit amet, consectetur adipiscing elit, sed do eiusmod tempor incididunt ut labore et dolore magna aliqua. Ut enim ad minim veniam, quis nostrud exercitation ullamco laboris nisi ut aliquip ex ea commodo consequat. Lorem ipsum dolor sit amet, consectetur adipiscing elit, sed do eiusmod tempor incididunt ut labore et dolore magna aliqua. Ut enim ad minim veniam, quis nostrud exercitation ullamco laboris nisi ut aliquip ex ea commodo consequat.</p>
    </div>
    <div class="item" style="left:139px;top:17px;width:90px"><svg class="icon" style="flex:none"><use href="#i-people"/></svg><div><div class="item-title">Lorem Ipsum</div><p class="body-text">Lorem ipsum dolor sit amet, consectetur adipiscing elit, sed do eiusmod tempor incididunt ut labore et dolore magna aliqua.</p></div></div>
    <div class="item" style="left:139px;top:57px;width:90px"><svg class="icon" style="flex:none"><use href="#i-doc"/></svg><div><div class="item-title">Lorem Ipsum</div><p class="body-text">Lorem ipsum dolor sit amet, consectetur adipiscing elit, sed do eiusmod tempor incididunt ut labore et dolore magna aliqua.</p></div></div>
    <div class="item" style="left:139px;top:95px;width:90px"><svg class="icon" style="flex:none"><use href="#i-play"/></svg><div><div class="item-title">Lorem Ipsum</div><p class="body-text">Lorem ipsum dolor sit amet, consectetur adipiscing elit, sed do eiusmod tempor incididunt ut labore et dolore magna aliqua.</p></div></div>
    <div class="abs" style="left:128px;right:8px;bottom:5px;height:.5px;background:#d5d8dc"></div>
  </section>

  <!-- 22 three navy cards -->
  <section class="slide">
    <h2 class="abs slide-title" style="left:14px;top:12px">EDIT TITLE HERE</h2>
    <div class="abs" style="left:17px;top:29px;width:66px;height:91px;background:var(--navy-deep);text-align:center;padding:18px 5px 0"><svg class="icon white" style="width:16px;height:16px"><use href="#i-calendar"/></svg><div class="item-title orange" style="margin:6px 0 2px">LOREM IPSUM DOLOR</div><p class="body-text light">Lorem ipsum dolor sit amet, consectetur adipiscing elit, sed do eiusmod.</p></div>
    <div class="abs" style="left:87px;top:29px;width:66px;height:91px;background:var(--navy-deep);text-align:center;padding:18px 5px 0"><svg class="icon white" style="width:16px;height:16px"><use href="#i-chart"/></svg><div class="item-title orange" style="margin:6px 0 2px">LOREM IPSUM DOLOR</div><p class="body-text light">Lorem ipsum dolor sit amet, consectetur adipiscing elit, sed do eiusmod.</p></div>
    <div class="abs" style="left:158px;top:29px;width:66px;height:91px;background:var(--navy-deep);text-align:center;padding:18px 5px 0"><svg class="icon white" style="width:16px;height:16px"><use href="#i-download"/></svg><div class="item-title orange" style="margin:6px 0 2px">LOREM IPSUM DOLOR</div><p class="body-text light">Lorem ipsum dolor sit amet, consectetur adipiscing elit, sed do eiusmod.</p></div>
  </section>

  <!-- 23 collage with long text -->
  <section class="slide">
    <div class="abs" style="left:12px;top:11px;width:94px;height:113px;display:grid;grid-template-columns:repeat(2,1fr);grid-template-rows:repeat(3,1fr);gap:1.5px">
      <div class="ph-office" role="img" aria-label="Overleg van bovenaf"></div>
      <div class="ph-people" role="img" aria-label="Team aan tafel"></div>
      <div class="ph-people" role="img" aria-label="Juichende medewerker"></div>
      <div class="ph-office" role="img" aria-label="Collega's in gesprek"></div>
      <div class="ph-office" role="img" aria-label="Medewerker achter laptop"></div>
      <div class="ph-people" role="img" aria-label="Vergadering"></div>
    </div>
    <h2 class="abs" style="left:122px;top:22px;font-size:6.6px;font-weight:600;color:var(--navy);line-height:1.3">Lorem ipsum dolor<br>sit amet, consectetur</h2>
    <p class="abs body-text" style="left:122px;top:43px;width:105px;color:#222">Lorem ipsum dolor sit amet, consectetur adipiscing elit, sed do eiusmod tempor incididunt ut labore et dolore magna aliqua. Ut enim ad minim veniam, quis nostrud exercitation ullamco laboris nisi ut aliquip ex ea commodo consequat. Lorem ipsum dolor sit amet, consectetur adipiscing elit, sed do eiusmod tempor incididunt ut labore et dolore magna aliqua. Ut enim ad minim veniam, quis nostrud exercitation ullamco laboris nisi ut aliquip ex ea commodo consequat.</p>
    <div class="abs logo" style="left:7px;bottom:4px;font-size:3px"><span class="dot" style="width:4px;height:4px"></span>Stroomwacht</div>
  </section>

  <!-- 24 thank you -->
  <section class="slide">
    <div class="photo" style="inset:0;background:linear-gradient(180deg,#8aa6c4 0%,#3f5f82 60%,#1d3656 100%)" role="img" aria-label="Kantoortorens van onderaf gezien"></div>
    <div class="abs bg-orange" style="left:54px;top:0;width:8px;height:134px"></div>
    <div class="abs bg-orange" style="left:184px;top:0;width:8px;height:134px"></div>
    <div class="abs bg-navy" style="left:62px;top:0;width:122px;height:134px;color:#fff;text-align:center">
      <h2 style="font-size:13px;font-weight:300;margin-top:34px;letter-spacing:.3px">THANK YOU</h2>
      <div style="width:90px;height:.5px;background:#fff;margin:3px auto 8px"></div>
      <div style="font-size:4.6px;font-weight:600;margin-bottom:6px">Stroomwacht</div>
      <div style="font-size:3.4px;line-height:1.4">Havenstraat 12<br>1014 BK Amsterdam</div>
      <div style="font-size:3.4px;margin-top:4px;display:flex;justify-content:space-between;padding:0 4px"><span>P: +31 20 555 01 48</span><span>www.stroomwacht.nl</span></div>
      <div class="logo" style="justify-content:center;color:#fff;margin-top:8px;font-size:3.6px"><span class="dot" style="background:#fff"></span>Stroomwacht</div>
    </div>
  </section>

</main>
</body>
</html>
```